Business Card Design Project

I am seeking a business card for my life coaching career. I specialize in coaching executives and entrepreneurs. Consciousness plays a key role in my practice.
Updates

I would like to see different fonts -I don't like the way the capital J looks. I only want my name once on the card, on the front. I like everything centered on the front, with a white background, grey and green on the front; and the same grey on the back with bullet points next to each quality; centered. I like a subtle shadow of the mountains behind the text on the back of the card. I don't want the mountains on either side to be too big. Thank you.

Target Market(s)

Middle age business owners/executives

Industry/Entity Type

Business

Contact Information for Business Card

The front design is my name and a mountain logo. I want to have my name prominently shown.

Requirements
Must have
• Front of card:
• My name prominent sized font
• Helping clients lead more fulfilling lives;
• Executive Life Coach
• 415-362-4807
• pkrelt4@mailvane.net
• Back of Card:
• Providing Unparalleled support
• Providing a safe place to grow in self-awareness
• 20+ years entrepreneurial experience
• Trust
• Integrity
Nice to have
• Easy to read font; warm colors reflecting a masculine personality.

```html
<!DOCTYPE html>
<html lang="en">
<head>
<meta charset="utf-8">
<title>Dale Marsh – Executive Life Coach Business Card</title>
<link rel="stylesheet" href="https://fonts.googleapis.com/css2?family=Oswald:wght@500;600&family=Arimo:wght@400&family=Saira+Semi+Condensed:wght@400;600&display=swap">
<style>
  :root {
    --stage: #e4e7e7;
    --stage-edge: #cfd3d3;
    --card-white: #ffffff;
    --brand-green: #3f7a1c;
    --forest: #2f6e1c;
    --lime: #8cf23a;
    --rule-green: #a9c296;
    --ink: #2a2a2a;
    --slate: #333333;
    --rule-grey: #8e8e8e;
    --paper-text: #f4f4f4;
  }
  * { margin: 0; padding: 0; box-sizing: border-box; }
  html, body { width: 1200px; height: 900px; overflow: hidden; }
  body {
    background: radial-gradient(ellipse at 50% 30%, var(--stage) 0%, var(--stage-edge) 100%);
    position: relative;
  }
  .card {
    position: absolute;
    top: 237px;
    width: 490px;
    height: 266px;
    overflow: hidden;
  }
  .card-front { left: 99px; background: var(--card-white); }
  .card-back { left: 611px; background: var(--slate); color: var(--paper-text); text-align: center; }

  .brand-mark {
    position: absolute;
    left: 13px; top: 32px;
    font-family: "Oswald", sans-serif;
    font-weight: 600;
    font-size: 18px;
    color: var(--brand-green);
    line-height: 1;
  }
  .identity {
    position: absolute;
    left: 169px; top: 24px;
    width: 306px;
    text-align: center;
  }
  .holder-name {
    font-family: "Oswald", sans-serif;
    font-weight: 500;
    font-size: 52px;
    line-height: 56px;
    letter-spacing: 1px;
    color: var(--brand-green);
    text-transform: uppercase;
  }
  .tagline {
    font-family: "Arimo", sans-serif;
    font-size: 14px;
    color: var(--ink);
    line-height: 16px;
    margin-top: -2px;
  }
  .role {
    font-family: "Arimo", sans-serif;
    font-size: 17px;
    color: var(--ink);
    border-top: 3px solid var(--rule-green);
    border-bottom: 3px solid var(--rule-green);
    padding: 3px 0 4px;
    margin-top: 3px;
    line-height: 20px;
  }
  .phone, .email {
    font-family: "Arimo", sans-serif;
    font-size: 20px;
    line-height: 22px;
    color: var(--ink);
  }
  .phone { margin-top: 4px; }
  .email { color: var(--brand-green); font-size: 19px; }
  .ridge { position: absolute; left: 0; top: 0; width: 490px; height: 266px; }

  .back-rule {
    position: absolute;
    left: 92px; width: 305px; height: 3px;
    background: var(--rule-grey);
  }
  .back-rule.top { top: 66px; }
  .back-rule.bottom { top: 182px; }
  .promise {
    position: absolute;
    top: 77px; left: 0; width: 490px;
    font-family: "Saira Semi Condensed", sans-serif;
    text-transform: uppercase;
  }
  .promise h2 {
    font-weight: 600;
    font-size: 21px;
    letter-spacing: 1px;
    line-height: 24px;
  }
  .promise ul { list-style: none; }
  .promise li {
    font-weight: 400;
    font-size: 13.5px;
    letter-spacing: 0.8px;
    line-height: 19px;
  }
</style>
</head>
<body>
  <section class="card card-front" aria-label="Business card front">
    <svg class="ridge" viewBox="0 0 490 266" aria-hidden="true">
      <defs>
        <linearGradient id="forestFill" x1="0" y1="0" x2="1" y2="1">
          <stop offset="0" stop-color="#3d7d22"/>
          <stop offset="1" stop-color="#27631a"/>
        </linearGradient>
      </defs>
      <polygon points="0,186 197,241 329,190 490,215 490,266 0,266" fill="url(#forestFill)"/>
      <polyline points="0,186 197,241 329,190 490,215" fill="none" stroke="var(--lime)" stroke-width="5"/>
    </svg>
    <div class="brand-mark">Dale Marsh</div>
    <div class="identity">
      <h1 class="holder-name">Dale Marsh</h1>
      <p class="tagline">Helping Clients lead more fulfilling lives.</p>
      <p class="role">EXECUTIVE LIFE COACH</p>
      <p class="phone">415-362-4807</p>
      <p class="email">pkrelt4@mailvane.net</p>
    </div>
  </section>

  <section class="card card-back" aria-label="Business card back">
    <div class="back-rule top"></div>
    <div class="promise">
      <h2>Providing Unparalleled Support</h2>
      <ul>
        <li>Providing a safe place to grow in self-awareness,</li>
        <li>20+ years entrepreneurial experience,</li>
        <li>Trust &amp;</li>
        <li>Integrity.</li>
      </ul>
    </div>
    <div class="back-rule bottom"></div>
  </section>
</body>
</html>
```